Company Proposal Powerpoint Template

We would like to update our overall proposal presentation with a fresh, new look that might appeal to the younger generation. We are a full-meeting management company that specializes in corporate events sales meetings, incentive trips, and tradeshows/conferences.
We have a core set of slides that we use for presentations, but will also need to customize based on the customers we service and what we are selling each potential client.
We have a company logo, but we are not tied into the colors schemes for the logo and are okay adding the logo in black or white versus in color.
I have included our current look and feel for this presentation. This will also give you content that we typically add to this presentation.
Reason: Traveling out of the office so limited access to review the art.
Industry/Entity Type
It Company
Look and feel

```html
<!DOCTYPE html>
<html lang="en">
<head>
<meta charset="utf-8">
<title>Company Proposal Presentation – Slide Overview</title>
<link href="https://fonts.googleapis.com/css2?family=Poppins:wght@400;500;600;700&family=Open+Sans:wght@400;600&display=swap" rel="stylesheet">
<style>
  :root{
    --canvas:#e2e1e0;
    --paper:#ffffff;
    --ink:#161616;
    --blue:#5b8fd6;
    --blue-soft:#8fb1e2;
    --dark-bar:#3c3c3c;
    --black-bar:#0f0f0f;
    --muted:#8c8c8c;
    --rule:#d6d6d6;
    --mark:#a8282d;
  }
  *{box-sizing:border-box;margin:0;padding:0}
  html,body{width:1200px;height:1200px;overflow:hidden;background:var(--canvas)}
  .sheet{position:relative;width:1200px;height:1200px}
  .slide{position:absolute;background:var(--paper);overflow:hidden}
  .title{position:absolute;left:27px;top:12px;font:600 13px/1 'Poppins',sans-serif;color:var(--ink)}
  .title span{color:var(--blue)}
  .page{position:absolute;right:26px;top:12px;font:600 3.6px/1 'Poppins',sans-serif;color:var(--ink)}
  .brand{position:absolute;right:10px;bottom:6px;display:flex;align-items:center;gap:2px;font:500 5.5px/1 'Poppins',sans-serif;color:#444}
  .brand i{display:block;width:6px;height:6px;border:1px solid var(--mark)}
  .copy{position:absolute;font:400 3.6px/1.5 'Open Sans',sans-serif;color:var(--muted)}
  .copy.c{text-align:center}
  .copy.j{text-align:justify}
  .label{position:absolute;font:600 4.6px/1 'Poppins',sans-serif;color:var(--ink)}
  .label.c{text-align:center}
  .btn{position:absolute;height:8px;border:1px solid var(--ink);font:600 2.8px/6px 'Open Sans',sans-serif;text-align:center;color:var(--ink)}
  .icon{position:absolute}
  .photo{position:absolute}
  .headline{position:absolute;font:700 18px/1.35 'Poppins',sans-serif;letter-spacing:.6px;color:var(--ink)}
  .headline span{display:block;color:var(--blue)}
  .headline.mono span{color:var(--ink)}
  .dash{position:absolute;width:22px;height:1px;background:#9a9a9a}
  .chart{position:absolute;overflow:visible}
  .overlay .title,.overlay .label{color:#fff}
  .overlay .copy{color:rgba(255,255,255,.75)}
  .overlay .btn{border-color:#fff;color:#fff}
  .thanks{position:absolute;left:0;right:0;top:80px;text-align:center;font:500 22px/1.1 'Poppins',sans-serif;letter-spacing:2px;color:#fff}
</style>
</head>
<body>
<div class="sheet">

  <!-- Our Services -->
  <section class="slide" style="left:22px;top:19px;width:334px;height:187px">
    <h2 class="title">Our <span>Services</span></h2>
    <div class="page">Page 36</div>
    <p class="copy" style="left:28px;top:32px;width:290px">Frequently, your initial font choice is taken out of your hands, companies often specify a typeface, or even a set of fonts, as part of their brand guidelines you'll find a job has specific requirements, such as limited room that might require a</p>
    <svg class="icon" style="left:38px;top:66px" width="22" height="22" viewBox="0 0 22 22"><rect x=".5" y=".5" width="21" height="21" fill="none" stroke="#888"/><rect x="5" y="7" width="12" height="8" fill="none" stroke="#666" stroke-width=".8"/><path d="M5 7l6 4 6-4" fill="none" stroke="#666" stroke-width=".8"/></svg>
    <svg class="icon" style="left:117px;top:66px" width="22" height="22" viewBox="0 0 22 22"><rect x=".5" y=".5" width="21" height="21" fill="none" stroke="#888"/><rect x="5" y="6" width="12" height="10" fill="none" stroke="#666" stroke-width=".8"/><path d="M5 14l4-4 3 3 2-2 3 3" fill="none" stroke="#666" stroke-width=".8"/></svg>
    <svg class="icon" style="left:196px;top:66px" width="22" height="22" viewBox="0 0 22 22"><rect x=".5" y=".5" width="21" height="21" fill="none" stroke="#888"/><path d="M6 13v-3a5 5 0 0 1 10 0v3" fill="none" stroke="#666" stroke-width=".8"/><rect x="5" y="12" width="3" height="4" fill="#666"/><rect x="14" y="12" width="3" height="4" fill="#666"/></svg>
    <svg class="icon" style="left:275px;top:66px" width="22" height="22" viewBox="0 0 22 22"><rect x=".5" y=".5" width="21" height="21" fill="none" stroke="#888"/><path d="M7 5v12M11 5v12M15 5v12" stroke="#666" stroke-width=".8"/><circle cx="7" cy="9" r="1.5" fill="#fff" stroke="#666" stroke-width=".8"/><circle cx="11" cy="13" r="1.5" fill="#fff" stroke="#666" stroke-width=".8"/><circle cx="15" cy="8" r="1.5" fill="#fff" stroke="#666" stroke-width=".8"/></svg>
    <div class="label c" style="left:19px;top:97px;width:60px">Message</div>
    <div class="label c" style="left:98px;top:97px;width:60px">Clear</div>
    <div class="label c" style="left:177px;top:97px;width:60px">Communication</div>
    <div class="label c" style="left:256px;top:97px;width:60px">Clean Design</div>
    <p class="copy c" style="left:24px;top:106px;width:50px">We've packed all the features you could want into one awesome kit</p>
    <p class="copy c" style="left:103px;top:106px;width:50px">We've packed all the features you could want into one awesome</p>
    <p class="copy c" style="left:182px;top:106px;width:50px">We've packed all the features you could want into one awesome</p>
    <p class="copy c" style="left:261px;top:106px;width:50px">We've packed all the features you could want into one awesome</p>
    <div class="btn" style="left:30px;top:141px;width:38px">Service 1</div>
    <div class="btn" style="left:109px;top:141px;width:38px">Service 2</div>
    <div class="btn" style="left:188px;top:141px;width:38px">Service 3</div>
    <div class="btn" style="left:267px;top:141px;width:38px">Service 4</div>
    <div class="brand"><i></i>Meridian Events</div>
  </section>

  <!-- Premium Services -->
  <section class="slide" style="left:406px;top:19px;width:335px;height:187px">
    <h2 class="title">Premium <span>Services</span></h2>
    <div class="page">Page 37</div>
    <svg class="chart" style="left:0;top:0" width="335" height="187" viewBox="0 0 335 187" fill="none" stroke="#333" stroke-width=".8">
      <g stroke="#333"><circle cx="63" cy="53" r="11"/><circle cx="134" cy="53" r="11" stroke="var(--blue)"/><circle cx="204" cy="53" r="11"/><circle cx="275" cy="53" r="11"/>
      <circle cx="63" cy="119" r="11"/><circle cx="134" cy="119" r="11"/><circle cx="204" cy="119" r="11"/><circle cx="275" cy="119" r="11" stroke="var(--blue)"/></g>
      <rect x="57" y="49" width="12" height="8"/><path d="M57 49l6 4 6-4"/>
      <circle cx="134" cy="53" r="5" stroke="var(--blue)"/><circle cx="134" cy="53" r="2" stroke="var(--blue)"/>
      <path d="M204 59l-5-5a3 3 0 0 1 5-4a3 3 0 0 1 5 4z"/>
      <path d="M275 47l5 9h-10z"/>
      <path d="M63 113v12M59 122a4 4 0 0 0 8 0M60 116h6"/>
      <path d="M131 125v-12h6l-2 3 2 3h-6"/>
      <rect x="198" y="114" width="12" height="10"/><path d="M198 122l4-4 3 3 2-2 3 3"/>
      <path d="M270 114l10 10M280 114l-10 10" stroke="var(--blue)"/>
    </svg>
    <div class="label c" style="left:33px;top:72px;width:60px">Improve</div>
    <div class="label c" style="left:104px;top:72px;width:60px">Improve</div>
    <div class="label c" style="left:174px;top:72px;width:60px">Improve</div>
    <div class="label c" style="left:245px;top:72px;width:60px">Improve</div>
    <p class="copy c" style="left:30px;top:79px;width:66px">We've packed all the features you could want into one awesome &amp; stunning presentation</p>
    <p class="copy c" style="left:101px;top:79px;width:66px">We've packed all the features you could want into one awesome &amp; stunning presentation</p>
    <p class="copy c" style="left:171px;top:79px;width:66px">We've packed all the features you could want into one awesome &amp; stunning presentation</p>
    <p class="copy c" style="left:242px;top:79px;width:66px">We've packed all the features you could want into one awesome &amp; stunning presentation</p>
    <div class="label c" style="left:33px;top:138px;width:60px">Improve</div>
    <div class="label c" style="left:104px;top:138px;width:60px">Improve</div>
    <div class="label c" style="left:174px;top:138px;width:60px">Improve</div>
    <div class="label c" style="left:245px;top:138px;width:60px">Improve</div>
    <p class="copy c" style="left:30px;top:145px;width:66px">We've packed all the features you could want into one awesome &amp; stunning presentation</p>
    <p class="copy c" style="left:101px;top:145px;width:66px">We've packed all the features you could want into one awesome &amp; stunning presentation</p>
    <p class="copy c" style="left:171px;top:145px;width:66px">We've packed all the features you could want into one awesome &amp; stunning presentation</p>
    <p class="copy c" style="left:242px;top:145px;width:66px">We've packed all the features you could want into one awesome &amp; stunning presentation</p>
    <div class="brand"><i></i>Meridian Events</div>
  </section>

  <!-- Premium Features -->
  <section class="slide" style="left:798px;top:19px;width:339px;height:190px">
    <h2 class="title">Premium <span>Features</span></h2>
    <div class="page">Page 40</div>
    <svg class="chart" style="left:0;top:0" width="339" height="190" viewBox="0 0 339 190" fill="none" stroke-width=".8">
      <rect x="25" y="52" width="14" height="10" stroke="#555"/><path d="M28 55h8M28 58h8" stroke="#555"/>
      <path d="M124 52h7l-3.5 6 3.5 6h-7l3.5-6z" stroke="var(--blue)"/>
      <circle cx="32" cy="120" r="6" stroke="#333"/><circle cx="32" cy="120" r="2.5" stroke="#333"/>
      <path d="M124 124h9a2.5 2.5 0 0 0 0-5a4 4 0 0 0-7-1a3 3 0 0 0-2 6z" stroke="#555"/>
    </svg>
    <div class="label" style="left:24px;top:76px">Improve</div>
    <div class="label" style="left:120px;top:76px">Deadline</div>
    <p class="copy j" style="left:24px;top:84px;width:88px">Frequently, your initial font choice is taken out of your hands companies often specify a typeface, or even a set of fonts, as part of their brand</p>
    <p class="copy j" style="left:120px;top:84px;width:90px">Frequently, your initial font choice is taken out of your hands companies often specify a typeface, or even a set of fonts, as part of their brand</p>
    <div class="label" style="left:24px;top:137px">Support</div>
    <div class="label" style="left:120px;top:137px">Cloud</div>
    <p class="copy j" style="left:24px;top:145px;width:88px">Frequently, your initial font choice is taken out of your hands companies often specify a typeface, or even a set of fonts, as part of their brand</p>
    <p class="copy j" style="left:120px;top:145px;width:90px">Frequently, your initial font choice is taken out of your hands companies often specify a typeface, or even a set of fonts, as part of their brand</p>
    <div class="photo" role="img" aria-label="Bright modern interior with tall windows" style="left:221px;top:52px;width:86px;height:116px;background:linear-gradient(160deg,#d9d6cf 0%,#b7b1a6 45%,#8e8676 75%,#5f5a55 100%)"></div>
    <div class="brand"><i></i>Meridian Events</div>
  </section>

  <!-- Awesome Features -->
  <section class="slide overlay" style="left:22px;top:246px;width:338px;height:190px">
    <div class="photo" role="img" aria-label="City skyline and river bridge under a blue tint" style="left:0;top:0;width:338px;height:190px;background:linear-gradient(180deg,#8fb0de 0%,#7a9fd4 45%,#6c92cc 70%,#7fa3d7 100%)"></div>
    <h2 class="title" style="color:#fff">Awesome Features</h2>
    <svg class="chart" style="left:0;top:0" width="338" height="190" viewBox="0 0 338 190" fill="none" stroke="#fff" stroke-width=".7">
      <rect x="43" y="67" width="14" height="12"/><rect x="46" y="70" width="8" height="6"/><path d="M46 70l4 3 4-3"/>
      <rect x="122" y="67" width="14" height="12"/><path d="M125 76l3-3 2 2 2-2 2 2"/>
      <rect x="201" y="67" width="14" height="12"/><path d="M204 75v-2a4 4 0 0 1 8 0v2"/>
      <rect x="279" y="67" width="14" height="12"/><path d="M283 69v8M286 69v8M289 69v8"/>
    </svg>
    <div class="label c" style="left:20px;top:89px;width:60px">Clean Design</div>
    <div class="label c" style="left:99px;top:89px;width:60px">Clean Design</div>
    <div class="label c" style="left:178px;top:89px;width:60px">Clean Design</div>
    <div class="label c" style="left:257px;top:89px;width:60px">Clean Design</div>
    <p class="copy c" style="left:25px;top:98px;width:50px">We've packed all the features you could want into one awesome</p>
    <p class="copy c" style="left:104px;top:98px;width:50px">We've packed all the features you could want into one awesome</p>
    <p class="copy c" style="left:183px;top:98px;width:50px">We've packed all the features you could want into one awesome</p>
    <p class="copy c" style="left:262px;top:98px;width:50px">We've packed all the features you could want into one awesome</p>
    <div class="btn" style="left:31px;top:134px;width:38px">Service 1</div>
    <div class="btn" style="left:110px;top:134px;width:38px">Service 2</div>
    <div class="btn" style="left:189px;top:134px;width:38px">Service 3</div>
    <div class="btn" style="left:268px;top:134px;width:38px">Service 4</div>
  </section>

  <!-- Our Projects (single) -->
  <section class="slide" style="left:406px;top:246px;width:339px;height:190px">
    <h2 class="title">Our <span>Projects</span></h2>
    <div class="page">Page 43</div>
    <div class="label" style="left:28px;top:51px;font-size:7px">Project X</div>
    <p class="copy j" style="left:28px;top:72px;width:130px">Frequently, your initial font choice is taken out of your hands: companies often specify a typeface, or even a set of fonts, as part of their brand guidelines. Occasionally you'll find a job has specific requirements, such as limited room that might require a condensed face, or a lot of legal text that might require a face that's highly legible at small sizes. However, if you find yourself with an entirely blank page, with unlimited options, the natural place to start is the largest proportion of text, and that is probably your body copy.</p>
    <p class="copy j" style="left:28px;top:133px;width:130px">When selecting a typeface for body text, your primary concern should be readability. Don't concern yourself with personality at this stage. I'm of the school of thought that believes that you're better off mastering a few typefaces.</p>
    <div class="photo" role="img" aria-label="River at sunset with a tower and bridge in silhouette" style="left:170px;top:45px;width:143px;height:117px;background:linear-gradient(180deg,#9aa9bf 0%,#c9c3a6 40%,#e7c77a 55%,#5c5a55 72%,#2f3440 100%)"></div>
    <div class="brand"><i></i>Meridian Events</div>
  </section>

  <!-- Our Projects (gallery) -->
  <section class="slide" style="left:798px;top:246px;width:346px;height:195px">
    <h2 class="title">Our <span>Projects</span></h2>
    <div class="page">Page 44</div>
    <div class="photo" role="img" aria-label="River and skyline at dusk" style="left:26px;top:48px;width:55px;height:44px;background:linear-gradient(180deg,#8d9bb0,#d8c285 55%,#3a3d44)"></div>
    <div class="photo" role="img" aria-label="Bright interior with windows" style="left:26px;top:97px;width:55px;height:75px;background:linear-gradient(160deg,#dcd8d0,#a79f92 60%,#6a625a)"></div>
    <div class="photo" role="img" aria-label="Black and white river skyline with bridge" style="left:86px;top:48px;width:234px;height:74px;background:linear-gradient(180deg,#e9e9e9 0%,#b9b9b9 45%,#4d4d4d 70%,#7c7c7c 100%)"></div>
    <div class="photo" role="img" aria-label="Skyline at sunset" style="left:86px;top:127px;width:55px;height:42px;background:linear-gradient(180deg,#8d9bb0,#e2c47c 55%,#343740)"></div>
    <div class="photo" role="img" aria-label="Skyline at sunset" style="left:146px;top:127px;width:55px;height:42px;background:linear-gradient(180deg,#96a4b6,#dcc07e 55%,#343740)"></div>
    <div class="photo" role="img" aria-label="Skyline at sunset" style="left:206px;top:127px;width:55px;height:42px;background:linear-gradient(180deg,#8d9bb0,#e0c27d 55%,#353841)"></div>
    <div class="photo" role="img" aria-label="Glass building facade" style="left:266px;top:127px;width:54px;height:42px;background:linear-gradient(135deg,#c9d6ec,#7f9ed0 55%,#e2e8f3)"></div>
    <div class="brand"><i></i>Meridian Events</div>
  </section>

  <!-- Pie Charts -->
  <section class="slide" style="left:22px;top:468px;width:342px;height:192px">
    <h2 class="title">Pie <span>Charts</span></h2>
    <div class="page">Page 50</div>
    <svg class="chart" style="left:0;top:0" width="342" height="192" viewBox="0 0 342 192" fill="none" stroke-width="3">
      <g stroke="#eeeeee"><circle cx="59" cy="86" r="24"/><circle cx="133" cy="86" r="24"/><circle cx="206" cy="86" r="24"/><circle cx="280" cy="86" r="24"/></g>
      <g stroke="var(--blue)" transform-origin="0 0">
        <circle cx="59" cy="86" r="24" stroke-dasharray="101 151" transform="rotate(-90 59 86)"/>
        <circle cx="133" cy="86" r="24" stroke-dasharray="56 151" transform="rotate(-90 133 86)"/>
        <circle cx="206" cy="86" r="24" stroke-dasharray="75 151" transform="rotate(-90 206 86)"/>
        <circle cx="280" cy="86" r="24" stroke-dasharray="131 151" transform="rotate(-90 280 86)"/>
      </g>
      <g font-family="Poppins,sans-serif" font-weight="600" font-size="5" fill="#161616" stroke="none" text-anchor="middle">
        <text x="59" y="88">67 %</text><text x="133" y="88">37 %</text><text x="206" y="88">50 %</text><text x="280" y="88">87 %</text>
      </g>
    </svg>
    <div class="label c" style="left:29px;top:121px;width:60px;font-size:3.8px">Design</div>
    <div class="label c" style="left:103px;top:121px;width:60px;font-size:3.8px">Design</div>
    <div class="label c" style="left:176px;top:121px;width:60px;font-size:3.8px">Design</div>
    <div class="label c" style="left:250px;top:121px;width:60px;font-size:3.8px">Design</div>
    <p class="copy c" style="left:32px;top:128px;width:54px">Frequently, your initial font choice is taken out of your hands companies</p>
    <p class="copy c" style="left:106px;top:128px;width:54px">Frequently, your initial font choice is taken out of your hands companies</p>
    <p class="copy c" style="left:179px;top:128px;width:54px">Frequently, your initial font choice is taken out of your hands companies</p>
    <p class="copy c" style="left:253px;top:128px;width:54px">Frequently, your initial font choice is taken out of your hands companies</p>
    <div class="brand"><i></i>Meridian Events</div>
  </section>

  <!-- Bar Charts (horizontal) -->
  <section class="slide" style="left:406px;top:468px;width:347px;height:195px">
    <h2 class="title">Bar <span>Charts</span></h2>
    <div class="page">Page 51</div>
    <svg class="chart" style="left:28px;top:62px" width="156" height="90" viewBox="0 0 156 90">
      <g fill="var(--dark-bar)"><rect x="14" y="3" width="112" height="3.5"/><rect x="14" y="25" width="96" height="3.5"/><rect x="14" y="47" width="74" height="3.5"/><rect x="14" y="69" width="88" height="3.5"/></g>
      <g fill="var(--blue)"><rect x="14" y="9" width="68" height="3.5"/><rect x="14" y="31" width="84" height="3.5"/><rect x="14" y="53" width="40" height="3.5"/><rect x="14" y="75" width="40" height="3.5"/></g>
      <g fill="var(--black-bar)"><rect x="14" y="15" width="36" height="3.5"/><rect x="14" y="37" width="27" height="3.5"/><rect x="14" y="59" width="27" height="3.5"/><rect x="14" y="81" width="14" height="3.5"/></g>
      <path d="M14 0v86h140" fill="none" stroke="var(--rule)" stroke-width=".5"/>
    </svg>
    <h3 class="headline mono" style="left:188px;top:52px">AWESOME<span>CHARTS</span></h3>
    <div class="dash" style="left:190px;top:106px"></div>
    <p class="copy j" style="left:190px;top:118px;width:128px">Frequently, your initial font choice is taken out of your hands: companies often specify a typeface, or even a set of fonts, as part of their brand guides However, if you find yourself with an entirely blank page, with unlimited options, the natural place to start is the largest proportion of text, and that is probably your body copy.</p>
    <div class="brand"><i></i>Meridian Events</div>
  </section>

  <!-- Creative Charts (spikes) -->
  <section class="slide" style="left:798px;top:468px;width:354px;height:199px">
    <h2 class="title" style="color:var(--ink)">Creative Charts</h2>
    <div class="page">Page 52</div>
    <h3 class="headline" style="left:30px;top:52px">AWESOME<span>CHARTS</span></h3>
    <div class="dash" style="left:32px;top:107px"></div>
    <p class="copy j" style="left:32px;top:118px;width:128px">Frequently, your initial font choice is taken out of your hands: companies often specify a typeface, or even a set of fonts, as part of their brand guides However, if you find yourself with an entirely blank page, with unlimited options, the natural place to start is the largest proportion of text, and that is probably your body copy.</p>
    <svg class="chart" style="left:212px;top:70px" width="120" height="90" viewBox="0 0 120 90">
      <g fill="var(--dark-bar)"><polygon points="0,1 105,5 0,9"/><polygon points="0,22 82,25 0,28"/><polygon points="0,42 76,45 0,48"/><polygon points="0,61 72,64 0,67"/></g>
      <g fill="var(--blue)"><polygon points="0,8 64,10 0,12"/><polygon points="0,27 88,29 0,31"/><polygon points="0,47 60,49 0,51"/><polygon points="0,66 64,68 0,70"/></g>
      <g fill="var(--black-bar)"><polygon points="0,11 76,14 0,17"/><polygon points="0,30 96,33 0,36"/><polygon points="0,50 48,53 0,56"/><polygon points="0,69 40,72 0,75"/></g>
      <path d="M0 0v80h115" fill="none" stroke="var(--rule)" stroke-width=".5"/>
    </svg>
    <div class="brand"><i></i>Meridian Events</div>
  </section>

  <!-- Creative Charts (lines) -->
  <section class="slide" style="left:22px;top:695px;width:347px;height:195px">
    <h2 class="title" style="color:var(--ink)">Creative Charts</h2>
    <div class="page">Page 53</div>
    <svg class="chart" style="left:25px;top:60px" width="150" height="86" viewBox="0 0 150 86">
      <g stroke="#eeeeee" stroke-width=".5"><path d="M0 0h130M0 10h130M0 20h130M0 30h130M0 40h130M0 50h130M0 60h130M0 70h130M0 80h130"/></g>
      <path d="M10 26C40 30 50 50 60 36S90 16 100 12" fill="none" stroke="var(--dark-bar)" stroke-width=".9"/>
      <path d="M10 60C30 55 50 56 60 42S80 36 100 40" fill="none" stroke="var(--blue)" stroke-width=".9"/>
      <path d="M10 66C30 60 50 56 60 52S80 50 100 50" fill="none" stroke="var(--black-bar)" stroke-width=".9"/>
      <g fill="var(--muted)"><rect x="135" y="34" width="3" height="1"/><rect x="135" y="38" width="3" height="1" fill="var(--blue)"/><rect x="135" y="42" width="3" height="1"/></g>
    </svg>
    <h3 class="headline" style="left:190px;top:38px">AWESOME<span>CHARTS</span></h3>
    <div class="dash" style="left:192px;top:93px"></div>
    <p class="copy j" style="left:192px;top:104px;width:128px">Frequently, your initial font choice is taken out of your hands: companies often specify a typeface, or even a set of fonts, as part of their brand guides However, if you find yourself with an entirely blank page, with unlimited options, the natural place to start is the largest proportion of text, and that is probably your body copy.</p>
    <div class="brand"><i></i>Meridian Events</div>
  </section>

  <!-- Creative Charts (area) -->
  <section class="slide" style="left:406px;top:695px;width:351px;height:198px">
    <h2 class="title" style="color:var(--ink)">Creative Charts</h2>
    <div class="page">Page 54</div>
    <h3 class="headline" style="left:30px;top:38px">AWESOME<span>CHARTS</span></h3>
    <div class="dash" style="left:32px;top:94px"></div>
    <p class="copy j" style="left:32px;top:105px;width:128px">Frequently, your initial font choice is taken out of your hands: companies often specify a typeface, or even a set of fonts, as part of their brand guides However, if you find yourself with an entirely blank page, with unlimited options, the natural place to start is the largest proportion of text, and that is probably your body copy.</p>
    <svg class="chart" style="left:198px;top:76px" width="135" height="82" viewBox="0 0 135 82">
      <polygon points="0,27 42,27 85,0 128,0 128,80 0,80" fill="var(--dark-bar)"/>
      <polygon points="0,62 42,52 85,34 128,38 128,80 0,80" fill="var(--blue)"/>
      <polygon points="0,70 42,66 85,62 128,62 128,80 0,80" fill="var(--black-bar)"/>
      <path d="M0 0v80h130" fill="none" stroke="var(--rule)" stroke-width=".5"/>
    </svg>
    <div class="brand"><i></i>Meridian Events</div>
  </section>

  <!-- Creative Charts (radar) -->
  <section class="slide" style="left:798px;top:695px;width:360px;height:202px">
    <h2 class="title" style="color:var(--ink)">Creative Charts</h2>
    <div class="page">Page 55</div>
    <h3 class="headline" style="left:30px;top:39px">AWESOME<span>CHARTS</span></h3>
    <div class="dash" style="left:32px;top:95px"></div>
    <p class="copy j" style="left:32px;top:106px;width:128px">Frequently, your initial font choice is taken out of your hands: companies often specify a typeface, or even a set of fonts, as part of their brand guides However, if you find yourself with an entirely blank page, with unlimited options, the natural place to start is the largest proportion of text, and that is probably your body copy.</p>
    <svg class="chart" style="left:200px;top:46px" width="122" height="122" viewBox="0 0 122 122" fill="none">
      <g stroke="#dddddd" stroke-width=".5"><polygon points="61,6 116,61 61,116 6,61"/><polygon points="61,20 102,61 61,102 20,61"/><polygon points="61,34 88,61 61,88 34,61"/><path d="M61 6v110M6 61h110"/></g>
      <polygon points="61,8 114,61 61,112 8,61" stroke="var(--dark-bar)" stroke-width=".9"/>
      <polygon points="61,24 100,61 61,94 22,61" stroke="var(--blue)" stroke-width=".9"/>
      <polygon points="61,38 84,61 61,84 38,61" stroke="var(--black-bar)" stroke-width=".9"/>
    </svg>
    <div class="brand"><i></i>Meridian Events</div>
  </section>

  <!-- Bar Charts (columns) -->
  <section class="slide" style="left:22px;top:922px;width:351px;height:197px">
    <h2 class="title" style="color:var(--ink)">Bar Charts</h2>
    <div class="page">Page 56</div>
    <svg class="chart" style="left:33px;top:72px" width="128" height="76" viewBox="0 0 128 76">
      <g fill="var(--black-bar)"><rect x="8" y="52" width="6" height="20"/><rect x="38" y="58" width="6" height="14"/><rect x="68" y="50" width="6" height="22"/><rect x="98" y="46" width="6" height="26"/></g>
      <g fill="var(--blue)"><rect x="14" y="42" width="6" height="30"/><rect x="44" y="48" width="6" height="24"/><rect x="74" y="22" width="6" height="50"/><rect x="104" y="30" width="6" height="42"/></g>
      <g fill="var(--dark-bar)"><rect x="20" y="24" width="6" height="48"/><rect x="50" y="28" width="6" height="44"/><rect x="80" y="14" width="6" height="58"/><rect x="110" y="6" width="6" height="66"/></g>
      <path d="M2 0v72h124" fill="none" stroke="var(--rule)" stroke-width=".5"/>
    </svg>
    <h3 class="headline" style="left:192px;top:44px">AWESOME<span>CHARTS</span></h3>
    <div class="dash" style="left:194px;top:100px"></div>
    <p class="copy j" style="left:194px;top:111px;width:128px">Frequently, your initial font choice is taken out of your hands: companies often specify a typeface, or even a set of fonts, as part of their brand guides However, if you find yourself with an entirely blank page, with unlimited options, the natural place to start is the largest proportion of text, and that is probably your body copy.</p>
    <div class="brand"><i></i>Meridian Events</div>
  </section>

  <!-- Bar Charts (wide) -->
  <section class="slide" style="left:406px;top:926px;width:359px;height:202px">
    <h2 class="title">Bar <span>Charts</span></h2>
    <div class="page">Page 57</div>
    <svg class="chart" style="left:56px;top:56px" width="252" height="120" viewBox="0 0 252 120">
      <g fill="var(--dark-bar)"><rect x="6" y="0" width="238" height="6"/><rect x="6" y="26" width="208" height="6"/><rect x="6" y="52" width="148" height="6"/><rect x="6" y="78" width="178" height="6"/></g>
      <g fill="var(--blue)"><rect x="6" y="7" width="148" height="6"/><rect x="6" y="33" width="178" height="6"/><rect x="6" y="59" width="90" height="6"/><rect x="6" y="85" width="90" height="6"/></g>
      <g fill="var(--black-bar)"><rect x="6" y="14" width="90" height="6"/><rect x="6" y="40" width="90" height="6"/><rect x="6" y="66" width="60" height="6"/><rect x="6" y="92" width="30" height="6"/></g>
      <path d="M6 -2v104h242" fill="none" stroke="var(--rule)" stroke-width=".5"/>
    </svg>
    <div class="brand"><i></i>Meridian Events</div>
  </section>

  <!-- Thank You -->
  <section class="slide" style="left:798px;top:926px;width:368px;height:207px">
    <div class="photo" role="img" aria-label="City skyline and river bridge under a blue tint" style="left:0;top:0;width:368px;height:207px;background:linear-gradient(180deg,#8eaedd 0%,#7b9fd3 45%,#6b90c9 68%,#7ea2d6 100%)"></div>
    <svg class="chart" style="left:46px;top:70px" width="30" height="20" viewBox="0 0 30 20"><path d="M0 20V0h30" fill="none" stroke="#fff" stroke-width=".6" opacity=".8"/></svg>
    <div class="thanks">THANK<br>YOU</div>
  </section>

</div>
</body>
</html>
```